Website design for new health & wellness company

We need our website to be designed in a user friendly way. Needs to be aesthetically pleasing to viewer and easy to navigate and upload content for our small team . The logo should be completely redesigned , please do not reference the current one thats on our site for a starting place. (included below though) We want to move away from that.

the website is : www.brightpathforward.com

We are a small group of writers/coaches who believe that to change the world you have to be the change and we provide tips/suggestions for every day life that if followed can make a huge difference in your life and overall being.

Target Market(s)

Men and women ages 22 to 50

Industry/Entity Type

Health And Wellness

Logo Text

Cultivate the life of your dreams

Coding

Coded - Design and coding required

Number of Pages Required

3 page

Font styles to use
Sans Serif

Colors

Designer to choose colors to be used in the design.

Requirements
Must have
• Easy to navigate. Mobile friendly. Gender neutral, should appeal to both.

```html
<!DOCTYPE html>
<html lang="en">
<head>
<meta charset="utf-8">
<title>About us – Brightpath Forward</title>
<link href="https://fonts.googleapis.com/css2?family=Open+Sans:wght@300;400;600;700&display=swap" rel="stylesheet">
<style>
:root{
  --bg:#e8e7e5;
  --teal:#1fae9a;
  --teal-light:#8fdcbf;
  --ink:#333333;
  --muted:#555555;
  --pink:#ef1f8f;
  --orange-a:#ffa06e;
  --orange-b:#ffc874;
  --peach:#fca56f;
  --sky:#3ec6f2;
  --mint:#8fdcbf;
  --footer:#2b2b2b;
  --white:#ffffff;
}
*{box-sizing:border-box;margin:0;padding:0}
html,body{width:1200px;height:2308px;overflow:hidden}
body{font-family:"Open Sans",Arial,sans-serif;background:var(--bg);color:var(--ink);position:relative}
.abs{position:absolute}

/* header */
.site-header{left:0;top:0;width:1200px;height:111px;background:var(--bg)}
.brand{left:125px;top:30px;display:flex;align-items:center;gap:10px}
.brand-dot{width:26px;height:26px;border-radius:50%;background:var(--teal)}
.brand-name{font-size:22px;font-weight:600;color:var(--teal);line-height:1.1;width:120px}
.search{left:924px;top:26px;width:145px;height:19px;border-radius:10px;background:var(--white)}
.search svg{position:absolute;right:8px;top:4px}
.main-nav{left:392px;top:66px;display:flex;gap:0;width:677px;justify-content:space-between;font-size:13px;letter-spacing:.6px;color:var(--ink)}
.main-nav .active{color:var(--teal)}

/* hero */
.hero{left:0;top:111px;width:1200px;height:338px;background:linear-gradient(180deg,#8da266 0%,#b4593f 45%,#3f6a2f 100%)}
.hero-title{left:0;top:208px;width:1200px;text-align:center;font-size:60px;font-weight:400;color:var(--white)}
.hero-sub{left:0;top:297px;width:1200px;text-align:center;font-size:22px;line-height:27px;color:var(--white)}

/* about */
.coach-heading{left:125px;top:510px;font-size:27px;font-weight:300;color:var(--teal)}
.coach-text{left:125px;width:606px;font-size:13.5px;line-height:22px;color:var(--ink)}
.coach-text.first{top:569px}
.coach-text.second{top:807px}
.quote{left:125px;top:712px;width:560px;font-size:21px;font-weight:300;line-height:24px;color:var(--teal);padding-left:40px}
.quote .mark{position:absolute;font-size:60px;font-weight:700;color:var(--teal-light);line-height:1}
.btn-learn{left:125px;top:890px;width:206px;height:48px;border:2px solid var(--teal-light);border-radius:24px;background:var(--teal);color:var(--white);font-size:18px;display:flex;align-items:center;justify-content:center}
.coach-photo{left:772px;top:515px;width:302px;height:305px;background:linear-gradient(135deg,#c7b79a,#e7ddd0 55%,#a07d57)}
.coach-card{left:772px;top:820px;width:302px;height:87px;background:var(--teal);color:var(--white);text-align:center;padding-top:18px}
.coach-card .name{font-size:20px}
.coach-card .role{font-size:15px}

/* approach */
.approach{left:0;top:1010px;width:1200px;height:636px;background:linear-gradient(135deg,var(--orange-a),var(--orange-b))}
.approach-title{left:0;top:1058px;width:1200px;text-align:center;font-size:44px;font-weight:300;color:var(--white)}
.card{top:1164px;width:304px;height:408px;background:var(--white);box-shadow:0 8px 20px rgba(0,0,0,.18);text-align:center}
.card-img{height:193px}
.card h3{font-size:22px;font-weight:400;color:var(--muted);margin-top:24px}
.card p{font-size:12.5px;line-height:22px;color:var(--muted);width:250px;margin:12px auto 0}
.card .btn{display:inline-flex;width:123px;height:34px;border-radius:17px;background:var(--pink);color:var(--white);font-size:13.5px;align-items:center;justify-content:center;margin-top:20px}

/* work */
.work-title{left:0;top:1700px;width:1200px;text-align:center;font-size:44px;font-weight:400;color:var(--ink)}
.work-item{top:1827px;width:320px;display:flex;gap:18px}
.work-icon{width:96px;height:96px;border-radius:50%;flex:none;display:flex;align-items:center;justify-content:center}
.work-item h4{font-size:25px;font-weight:400;color:var(--ink);margin-top:-4px}
.work-item p{font-size:13px;line-height:19px;color:var(--ink);width:190px;margin-top:6px}

/* promo */
.promo-photo{left:0;top:2038px;width:495px;height:208px;background:linear-gradient(135deg,#5a3b2c,#c0392b 45%,#e3d6c5)}
.promo{left:495px;top:2038px;width:705px;height:208px;background:var(--mint)}
.promo h2{position:absolute;left:77px;top:50px;font-size:26px;font-weight:400;color:var(--white)}
.promo p{position:absolute;left:77px;top:98px;width:440px;font-size:12.5px;line-height:20px;color:var(--white)}

/* footer */
.site-footer{left:0;top:2246px;width:1200px;height:62px;background:var(--footer)}
.copyright{left:125px;top:2267px;font-size:13px;color:var(--white)}
.social{left:890px;top:2264px;display:flex;gap:16px}
.social span{width:27px;height:27px;border-radius:50%;background:#8a8a8a;display:block}
</style>
</head>
<body>

<header class="abs site-header"></header>
<div class="abs brand"><span class="brand-dot"></span><span class="brand-name">Brightpath Forward</span></div>
<div class="abs search"><svg width="12" height="12" viewBox="0 0 12 12"><circle cx="5" cy="5" r="3.5" fill="none" stroke="#ccc" stroke-width="1.5"/><line x1="7.5" y1="7.5" x2="11" y2="11" stroke="#ccc" stroke-width="1.5"/></svg></div>
<nav class="abs main-nav">
  <span class="active">HOME</span><span>ABOUT US</span><span>WORK WITH US</span><span>SUCCESS STORIES</span><span>BLOG</span><span>CONNECT</span><span>MORE</span>
</nav>

<section class="abs hero" role="img" aria-label="Photo of fresh vegetables: peppers, tomatoes, broccoli and greens"></section>
<h1 class="abs hero-title">About us</h1>
<p class="abs hero-sub">Helping you feel better about<br>your body and your life.</p>

<h2 class="abs coach-heading">As a coach, I put the power back in YOUR hands.</h2>
<p class="abs coach-text first">Lorem ipsum dolor sit amet, consectetur adipiscing elit. Mauris sagittis leo sed ex gravida rhoncus. Nam auctor enim vel elit tempor, et tempor massa commodo. Vestibulum orci sem, accumsan vitae tortor nec, dignissim fringilla massa. Sed varius placerat consectetur. Fusce lacus ligula, pharetra non ornare a, accumsan vel augue. Praesent malesuada vel augue vitae venenatis. Morbi id sapien sed vell.</p>
<blockquote class="abs quote"><span class="mark" style="left:0;top:-10px">“</span>I believe that we are a combination of the things we eat and the way we treat ourselves...<span class="mark" style="left:388px;top:22px">”</span></blockquote>
<p class="abs coach-text second">Through my programs, I give women super-practical, actionable guidance so they can feel great, take care of their bodies, and actually enjoy the process.</p>
<a class="abs btn-learn">LEARN MORE</a>
<div class="abs coach-photo" role="img" aria-label="Portrait photo of the health coach in a kitchen"></div>
<div class="abs coach-card"><div class="name">Corin Abeyta</div><div class="role">Health Coach</div></div>

<section class="abs approach"></section>
<h2 class="abs approach-title">A Fresh Approach for Health &amp; Wellness</h2>
<article class="abs card" style="left:125px">
  <div class="card-img" role="img" aria-label="Photo of orange juice and blood oranges" style="background:linear-gradient(135deg,#f08a1c,#e9a64a 50%,#6b4a2e)"></div>
  <h3>1:1 Consultation</h3>
  <p>Monthly sessions where we uncover the habits &amp; thoughts in the way of a healthy relationship with food &amp; your body.</p>
  <a class="btn">Learn More</a>
</article>
<article class="abs card" style="left:448px">
  <div class="card-img" role="img" aria-label="Photo of a woman at a table with fresh juices" style="background:linear-gradient(135deg,#8a7d6e,#d9d2c8 50%,#c24b3a)"></div>
  <h3>30 Day Challenge</h3>
  <p>You want to curb your cravings and discover a healthier lifestyle during a fun + simple 30 day online challenge.</p>
  <a class="btn">Learn More</a>
</article>
<article class="abs card" style="left:771px">
  <div class="card-img" role="img" aria-label="Photo of a group coaching session" style="background:linear-gradient(135deg,#b9b3ad,#d95a4a 50%,#5c5a66)"></div>
  <h3>Group Coaching</h3>
  <p>You're ready to explore a life that loves you as much as you love it through bi-weekly one on one coaching sessions.</p>
  <a class="btn">Learn More</a>
</article>

<h2 class="abs work-title">Work with us</h2>
<div class="abs work-item" style="left:125px">
  <div class="work-icon" style="background:var(--peach)"><svg width="44" height="44" viewBox="0 0 44 44" fill="none" stroke="#fff" stroke-width="2"><rect x="6" y="4" width="24" height="32" rx="2"/><line x1="11" y1="12" x2="25" y2="12"/><line x1="11" y1="19" x2="25" y2="19"/><line x1="11" y1="26" x2="20" y2="26"/><rect x="24" y="26" width="14" height="12" rx="2"/></svg></div>
  <div><h4>Programs</h4><p>Lorem ipsum dolor sit amet, consectetur adipiscing elit, sed do eiusmod tempor incididunt</p></div>
</div>
<div class="abs work-item" style="left:461px">
  <div class="work-icon" style="background:var(--sky)"><svg width="44" height="44" viewBox="0 0 44 44" fill="none" stroke="#fff" stroke-width="2"><rect x="6" y="9" width="32" height="28" rx="2"/><line x1="6" y1="16" x2="38" y2="16"/><line x1="13" y1="5" x2="13" y2="12"/><line x1="31" y1="5" x2="31" y2="12"/><g fill="#fff" stroke="none"><rect x="11" y="21" width="4" height="4"/><rect x="20" y="21" width="4" height="4"/><rect x="29" y="21" width="4" height="4"/><rect x="11" y="29" width="4" height="4"/><rect x="20" y="29" width="4" height="4"/></g></svg></div>
  <div><h4>Events</h4><p>Lorem ipsum dolor sit amet, consectetur adipiscing elit, sed do eiusmod tempor incididunt</p></div>
</div>
<div class="abs work-item" style="left:798px">
  <div class="work-icon" style="background:var(--mint)"><svg width="44" height="44" viewBox="0 0 44 44" fill="none" stroke="#fff" stroke-width="2"><path d="M14 10h14l-3 28h-8z"/><line x1="24" y1="4" x2="21" y2="20"/><line x1="6" y1="38" x2="38" y2="38"/></svg></div>
  <div><h4>Recipes</h4><p>Lorem ipsum dolor sit amet, consectetur adipiscing elit, sed do eiusmod tempor incididunt</p></div>
</div>

<div class="abs promo-photo" role="img" aria-label="Photo of strawberries, juice and grapefruit on a table"></div>
<section class="abs promo">
  <h2>Change your health in one day!</h2>
  <p>Learn 5 small but life changing daily habits that will have an immediate positive impact on your health. Learn 5 small but life changing daily habits that will have an immediate positive impact on your health!</p>
</section>

<footer class="abs site-footer"></footer>
<p class="abs copyright">Copyright ©2016 all rights reserved</p>
<div class="abs social"><span></span><span></span><span></span><span></span><span></span></div>

</body>
</html>
```